Design a Business Card for a restaurant ( 2 sides)

I need design for restaurant.

In the files you will see the content ( see the [login to view URL]) of the first side and link to the website of the restaurant. Please don't use black. The colors we prefer are red and gold like in the file: logo.jpg. I want you also use the symbol of "Trong Dong" , more see. [login to view URL] , in the visit cards as relief coating ( see photo)

In the backside, i want to have 10 places to stamp on it, when customer eat by us. And small text in the bottom " Liegt die Rechung über 20 Euro erhalten Sie einen Stempel von uns. Wenn Sie 10 Stempel gesammelt haben, gibt es einen Gutschein im Wert von 20 Euro."

Upload your desing with Mockup will increase your chance to win.

Be CREATIVE . Thanks.

```html
<!DOCTYPE html>
<html lang="de">
<head>
<meta charset="utf-8">
<title>Sen Vang – Visitenkarte</title>
<link rel="stylesheet" href="https://fonts.googleapis.com/css2?family=Source+Sans+3:wght@400;600&family=Roboto+Condensed:wght@400&display=swap">
<style>
  :root {
    --page-bg: #d9d7df;
    --card-red: #8e1a1e;
    --card-red-deep: #7a1418;
    --gold: #e3b94a;
    --gold-light: #f6de7c;
    --gold-dark: #b98a22;
    --logo-red: #7c1a14;
  }
  * { box-sizing: border-box; margin: 0; padding: 0; }
  html, body {
    width: 1200px; height: 1020px; overflow: hidden;
    background: var(--page-bg);
  }
  .canvas {
    position: relative; width: 1200px; height: 1020px;
  }
  .card {
    position: absolute; left: 220px; width: 760px; height: 440px;
    background: var(--card-red);
    box-shadow: 0 6px 18px rgba(0,0,0,.18);
    overflow: hidden;
  }
  /* Back side: stamp card */
  .card-back { top: 50px; }
  .back-band {
    position: absolute; left: 0; top: 0; bottom: 0; width: 190px;
    background: linear-gradient(90deg, var(--gold-dark), var(--gold-light) 45%, var(--gold) 100%);
    display: flex; align-items: center; justify-content: center;
  }
  .band-brand {
    font-family: "Source Sans 3", sans-serif; font-weight: 600;
    font-size: 30px; color: var(--logo-red); letter-spacing: .5px;
  }
  .stamp-grid {
    position: absolute; left: 250px; top: 52px;
    display: grid; grid-template-columns: repeat(5, 86px); gap: 16px 18px;
  }
  .stamp-box {
    width: 86px; height: 86px;
    border: 2px solid var(--gold);
  }
  .stamp-note {
    position: absolute; left: 190px; right: 0; top: 300px;
    text-align: center;
    font-family: "Roboto Condensed", sans-serif; font-size: 15px;
    line-height: 1.7; color: var(--gold);
  }
  /* Front side: contact card */
  .card-front {
    top: 540px;
    background: linear-gradient(135deg, var(--gold-light), var(--gold-dark));
    padding: 9px;
  }
  .front-panel {
    position: relative; width: 100%; height: 100%;
    background: var(--card-red);
  }
  .brand-name {
    position: absolute; left: 42px; top: 170px;
    font-family: "Source Sans 3", sans-serif; font-weight: 600;
    font-size: 54px; line-height: 1; color: var(--gold);
  }
  .brand-tagline {
    position: absolute; left: 44px; top: 232px;
    font-family: "Source Sans 3", sans-serif; font-weight: 600;
    font-size: 17px; color: var(--gold);
  }
  .contact {
    position: absolute; left: 42px; top: 284px;
    font-family: "Source Sans 3", sans-serif; color: var(--gold);
  }
  .contact-title { font-size: 24px; font-weight: 400; margin-bottom: 4px; }
  .contact-line { font-size: 16px; line-height: 1.35; }
  .drum-emblem {
    position: absolute; right: 40px; top: 40px;
    width: 330px; height: 330px;
  }
</style>
</head>
<body>
<main class="canvas">

  <section class="card card-back" aria-label="Stempelkarte">
    <div class="back-band">
      <span class="band-brand">Sen Vang</span>
    </div>
    <div class="stamp-grid">
      <div class="stamp-box"></div><div class="stamp-box"></div><div class="stamp-box"></div><div class="stamp-box"></div><div class="stamp-box"></div>
      <div class="stamp-box"></div><div class="stamp-box"></div><div class="stamp-box"></div><div class="stamp-box"></div><div class="stamp-box"></div>
    </div>
    <p class="stamp-note">
      Liegt die Rechung über 20 Euro erhalten Sie einen Stempel von uns<br>
      Wenn Sie 10 Stempel gesammelt haben, gibt es einen Gutschein im Wert von 20 Euro
    </p>
  </section>

  <section class="card card-front" aria-label="Visitenkarte Vorderseite">
    <div class="front-panel">
      <div class="brand-name">Sen Vang</div>
      <div class="brand-tagline">Original Vietnamesische Küche</div>
      <div class="contact">
        <p class="contact-title">Sen Vang Vietnam Restaurant</p>
        <p class="contact-line">Lindenweg 12, 30159 Hannover</p>
        <p class="contact-line">P : 49 511 555 014 20</p>
        <p class="contact-line">W : www.senvang-hannover.de</p>
      </div>
      <svg class="drum-emblem" viewBox="0 0 330 330" role="img" aria-label="Goldenes Bronzetrommel-Ornament mit Landkarte als Reliefprägung">
        <defs>
          <radialGradient id="emblemGold" cx="50%" cy="50%" r="50%">
            <stop offset="0%" stop-color="#f3d46a"/>
            <stop offset="60%" stop-color="#c9962c"/>
            <stop offset="100%" stop-color="#a87820"/>
          </radialGradient>
        </defs>
        <circle cx="165" cy="165" r="160" fill="url(#emblemGold)" opacity=".55"/>
      </svg>
    </div>
  </section>

</main>
</body>
</html>
```